'Cradle Ahead' promotional brochure

We have designed a 6 week program to educate impending first-time parents about the things they need to know to survive the first 6 months. Sessions delivered by general practitioner/family doctor, dietician, physiotherapist, speech pathologist and psychologist. Our promotional blurb is: 'A comprehensive education program for first-time parents-to-be, delivered over 6 weeks by health professionals in your community, about everything you need to know to look after your baby (and yourself!) in the first 6 months'. I now want to put together a promotional brochure to be distributed to those couples who express an interest which will provide further details of what will be delivered in the course.
Updates
In terms of layout, I envisaged a double sided A4 size, foldable into 3 sections, but very happy to be guided on this.
Target Market(s)
To appeal to a young, well educated demographic. First time parents couples.
Industry/Entity Type
Medical
Font styles to use
Other font styles liked:
- Playfair Display
Requirements
Must have
- Playfair display font to be consistent with our logo (attached). Logo also included please. Some consistency with colours of logo please.
Nice to have
- I am a doctor, and have no creative genes! But prefer a clean and professional appearance overall. Not too cluttered in overall appearance.
Should not have
- No cheesy pictures of babies.

```html
<!DOCTYPE html>
<html lang="en">
<head>
<meta charset="utf-8">
<title>Cradle Ahead – Brochure</title>
<link href="https://fonts.googleapis.com/css2?family=Playfair+Display:ital,wght@0,400;0,700;1,400&family=Lato:wght@400;700&display=swap" rel="stylesheet">
<style>
  :root{
    --green:#6bbb35;
    --green-dark:#58a329;
    --grey:#7b7b7b;
    --grey-dark:#6a6a6a;
    --grey-light:#d9d9d9;
    --text:#6d6d6d;
    --paper:#ffffff;
    --backdrop:#e5e5e5;
    --serif:'Playfair Display', Georgia, serif;
    --sans:'Lato', Arial, sans-serif;
  }
  *{box-sizing:border-box;margin:0;padding:0}
  html,body{width:1200px;height:2398px;overflow:hidden}
  body{background:var(--backdrop);font-family:var(--sans);color:var(--text)}
  .stage{height:799px;display:flex;align-items:center;justify-content:center}

  .sheet{display:flex;height:735px;background:var(--paper);box-shadow:0 6px 18px rgba(0,0,0,.12)}
  .panel{position:relative;width:347px;height:735px;overflow:hidden;background:var(--paper)}
  .panel__art{position:absolute;inset:0;width:100%;height:100%}
  .panel__content{position:relative;z-index:1}

  /* brand name */
  .brand{display:flex;align-items:center;gap:12px}
  .brand__dot{width:40px;height:40px;border-radius:50%;background:var(--green);flex:none}
  .brand__name{font-family:var(--serif);font-weight:400;color:var(--green);font-size:17px;line-height:1.1;letter-spacing:.06em;text-transform:uppercase}

  /* cover */
  .cover .brand{position:absolute;top:48px;left:40px}
  .cover__title{position:absolute;left:0;right:0;bottom:52px;text-align:center;font-family:var(--serif);color:#fff;font-size:30px;letter-spacing:.08em;text-transform:uppercase}

  /* intro flap */
  .intro .brand{position:absolute;top:40px;left:34px}
  .intro__body{position:absolute;top:128px;left:34px;right:30px}
  .intro__title{font-family:var(--serif);color:var(--green);font-size:29px;letter-spacing:.06em;text-transform:uppercase;margin-bottom:16px}
  .intro__lead{font-family:var(--serif);font-size:12px;letter-spacing:.08em;text-transform:uppercase;color:var(--grey-dark);line-height:1.45;margin-bottom:14px}
  .intro__line{font-family:var(--serif);font-style:italic;color:var(--green);font-size:13.5px;line-height:1.5;margin-bottom:10px}
  .intro__cost{font-family:var(--serif);color:var(--green);font-size:12px;letter-spacing:.1em;text-transform:uppercase;margin-top:14px}

  /* contact */
  .contact{background:var(--grey)}
  .contact__body{position:absolute;top:44px;left:38px;right:30px;color:#fff}
  .contact__title{font-family:var(--serif);font-size:17px;letter-spacing:.06em;text-transform:uppercase;line-height:1.35;margin-bottom:22px}
  .contact__org{font-family:var(--serif);font-size:13px;letter-spacing:.08em;text-transform:uppercase;line-height:1.35;margin-bottom:8px}
  .contact__text{font-size:11px;line-height:1.55}
  .contact__phone{font-size:13px;margin:12px 0 10px;letter-spacing:.04em}
  .contact__web{position:absolute;left:0;right:0;bottom:34px;text-align:center;color:#fff;font-size:13px;letter-spacing:.04em}

  /* inside panels */
  .inside .panel{background:transparent}
  .inside{position:relative}
  .inside__art{position:absolute;inset:0;width:1041px;height:735px}
  .inside__band-title{position:absolute;top:38px;left:347px;width:347px;text-align:center;font-family:var(--serif);color:#fff;font-size:28px;letter-spacing:.06em;text-transform:uppercase;z-index:1}
  .weeks{position:absolute;left:28px;right:26px}
  .week{margin-bottom:14px}
  .week__title{font-family:var(--serif);color:var(--green);font-size:17px;letter-spacing:.06em;text-transform:uppercase;border-bottom:1px solid var(--grey-light);padding-bottom:4px;margin-bottom:7px}
  .week__text{font-size:10.2px;line-height:1.5;margin-bottom:5px}
  .session{color:var(--green);font-weight:700}
  .week__list{list-style:none;font-size:10.2px;line-height:1.55}
  .week__list li{position:relative;padding-left:13px}
  .week__list li::before{content:"";position:absolute;left:0;top:5px;width:5px;height:5px;border-radius:50%;background:var(--green)}
  .week__list--cols{columns:2;column-gap:14px}
</style>
</head>
<body>

<!-- Front cover -->
<section class="stage">
  <div class="sheet">
    <article class="panel cover">
      <svg class="panel__art" viewBox="0 0 347 735" aria-hidden="false">
        <rect width="347" height="735" fill="#fff"/>
        <defs>
          <linearGradient id="coverPhoto" x1="0" y1="0" x2="1" y2="1">
            <stop offset="0" stop-color="#d4d4d4"/><stop offset=".55" stop-color="#a9a9a9"/><stop offset="1" stop-color="#efefef"/>
          </linearGradient>
        </defs>
        <path role="img" aria-label="Black and white photograph of a mother holding her baby" d="M0,238 Q160,178 347,125 L347,640 L0,640 Z" fill="url(#coverPhoto)"/>
        <path d="M0,205 Q150,150 347,98 L347,125 Q160,178 0,238 Z" fill="var(--green)"/>
        <path d="M0,612 Q180,556 347,566 L347,585 Q180,576 0,632 Z" fill="#e2e2e2"/>
        <path d="M0,630 Q180,572 347,584 L347,735 L0,735 Z" fill="var(--green)"/>
      </svg>
      <div class="brand"><span class="brand__dot"></span><span class="brand__name">Wattle Grove<br>Family Clinic</span></div>
      <h1 class="cover__title">Cradle Ahead</h1>
    </article>
  </div>
</section>

<!-- Outside spread -->
<section class="stage">
  <div class="sheet">
    <article class="panel intro">
      <svg class="panel__art" viewBox="0 0 347 735">
        <defs>
          <linearGradient id="handsPhoto" x1="0" y1="0" x2="1" y2="1">
            <stop offset="0" stop-color="#cfcfcf"/><stop offset=".5" stop-color="#9d9d9d"/><stop offset="1" stop-color="#dcdcdc"/>
          </linearGradient>
        </defs>
        <path role="img" aria-label="Black and white photograph of parents' hands around a baby's feet" d="M0,560 Q180,520 347,470 L347,735 L0,735 Z" fill="url(#handsPhoto)"/>
        <path d="M0,548 Q180,508 347,458 L347,470 Q180,520 0,560 Z" fill="var(--green)"/>
      </svg>
      <div class="brand"><span class="brand__dot"></span><span class="brand__name">Wattle Grove<br>Family Clinic</span></div>
      <div class="intro__body">
        <h2 class="intro__title">Cradle Ahead</h2>
        <p class="intro__lead">A comprehensive education program for first-time parents-to-be</p>
        <p class="intro__line">Delivered over 6 weeks by health professionals in your community</p>
        <p class="intro__line">Everything you need to know to look after your baby (and yourself!) in the first 6 months</p>
        <p class="intro__cost">Total cost $80</p>
      </div>
    </article>

    <article class="panel contact">
      <svg class="panel__art" viewBox="0 0 347 735">
        <circle cx="300" cy="40" r="150" fill="none" stroke="#8d8d8d" stroke-width="1.5"/>
        <circle cx="20" cy="500" r="170" fill="none" stroke="#8d8d8d" stroke-width="1.5"/>
        <circle role="img" aria-label="Street map showing the clinic location" cx="150" cy="470" r="82" fill="#d6d6d6"/>
        <path d="M0,640 Q180,600 347,615 L347,735 L0,735 Z" fill="var(--green)"/>
      </svg>
      <div class="contact__body">
        <h2 class="contact__title">Contact details for enquiries &amp; bookings</h2>
        <p class="contact__org">Wattle Grove<br>Family Clinic</p>
        <p class="contact__text">Lakeview Village, Shop 4<br>12 Harbour Way<br>Lakeview NSW 2400</p>
        <p class="contact__phone">02 5550 1234</p>
        <p class="contact__text">hello@wattlegroveclinic.example</p>
      </div>
      <p class="contact__web">www.wattlegroveclinic.example</p>
    </article>

    <article class="panel cover">
      <svg class="panel__art" viewBox="0 0 347 735">
        <rect width="347" height="735" fill="#fff"/>
        <defs>
          <linearGradient id="coverPhoto2" x1="0" y1="0" x2="1" y2="1">
            <stop offset="0" stop-color="#d4d4d4"/><stop offset=".55" stop-color="#a9a9a9"/><stop offset="1" stop-color="#efefef"/>
          </linearGradient>
        </defs>
        <path role="img" aria-label="Black and white photograph of a mother holding her baby" d="M0,238 Q160,178 347,125 L347,640 L0,640 Z" fill="url(#coverPhoto2)"/>
        <path d="M0,205 Q150,150 347,98 L347,125 Q160,178 0,238 Z" fill="var(--green)"/>
        <path d="M0,612 Q180,556 347,566 L347,585 Q180,576 0,632 Z" fill="#e2e2e2"/>
        <path d="M0,630 Q180,572 347,584 L347,735 L0,735 Z" fill="var(--green)"/>
      </svg>
      <div class="brand"><span class="brand__dot"></span><span class="brand__name">Wattle Grove<br>Family Clinic</span></div>
      <h2 class="cover__title">Cradle Ahead</h2>
    </article>
  </div>
</section>

<!-- Inside spread -->
<section class="stage">
  <div class="sheet inside">
    <svg class="inside__art" viewBox="0 0 1041 735">
      <defs>
        <linearGradient id="feetPhoto" x1="0" y1="0" x2="1" y2="1">
          <stop offset="0" stop-color="#e6e6e6"/><stop offset="1" stop-color="#9e9e9e"/>
        </linearGradient>
        <linearGradient id="babyPhoto" x1="0" y1="0" x2="1" y2="0">
          <stop offset="0" stop-color="#f2f2f2"/><stop offset=".5" stop-color="#c2c2c2"/><stop offset="1" stop-color="#f4f4f4"/>
        </linearGradient>
      </defs>
      <rect width="1041" height="735" fill="#fff"/>
      <path d="M0,0 H1041 V100 Q860,140 694,118 Q520,96 347,130 Q170,160 0,150 Z" fill="var(--grey)"/>
      <circle cx="520" cy="-60" r="190" fill="none" stroke="#8e8e8e" stroke-width="1.5"/>
      <circle cx="880" cy="-40" r="150" fill="none" stroke="#8e8e8e" stroke-width="1.5"/>
      <path d="M0,18 H150 A88,88 0 0 1 150,196 H0 Z" fill="var(--green)"/>
      <path role="img" aria-label="Black and white photograph of a newborn's feet" d="M0,26 H146 A80,80 0 0 1 146,186 H0 Z" fill="url(#feetPhoto)"/>
      <rect role="img" aria-label="Black and white photograph of a baby under a soft towel" x="410" y="590" width="225" height="125" rx="6" fill="url(#babyPhoto)"/>
    </svg>
    <h2 class="inside__band-title">Cradle Ahead</h2>

    <article class="panel">
      <div class="weeks" style="top:220px">
        <section class="week">
          <h3 class="week__title">Week 1</h3>
          <p class="week__text">GP Dr Lena Marsh will share information for new Mums about health after delivery. Topics include:</p>
          <ul class="week__list">
            <li>Vaccinations in pregnancy</li>
            <li>Bleeding, bladder and bowels after delivery</li>
            <li>Breastfeeding, engorgement and mastitis</li>
            <li>Bottle feeding</li>
            <li>Post-natal anxiety &amp; depression</li>
            <li>Intimacy and contraception</li>
          </ul>
        </section>
        <section class="week">
          <h3 class="week__title">Week 2</h3>
          <p class="week__text"><span class="session">Session 1 –</span> Clinical Psychologist Dr Owen Hale will discuss changes in relationships as couples become parents, gender roles in parenting and post-natal depression.</p>
          <p class="week__text"><span class="session">Session 2 –</span> Physiotherapist Tessa Ward will present advice for Mums regarding exercise during and after pregnancy, looking after the pelvic floor and abdominal muscle separation. She will also give advice on babies' neck strength, minimising flat spots on the head and encouraging gross motor skills in the first 6 months.</p>
        </section>
      </div>
    </article>

    <article class="panel">
      <div class="weeks" style="top:160px">
        <section class="week">
          <h3 class="week__title">Week 3</h3>
          <p class="week__text"><span class="session">Session 1 –</span> Dietician Nora Quill will provide advice for Mums regarding healthy eating during pregnancy and lactation, losing weight after delivery, breastfeeding, formula feeding and introducing solids, including foods with potential for allergy.</p>
          <p class="week__text"><span class="session">Session 2 –</span> Paediatric Speech Pathologist Jane Corbett will share information about sucking and swallowing, early communication, tongue tie and ways to encourage language development, including reading, talking and singing to your baby in the first 6 months.</p>
        </section>
      </div>
    </article>

    <article class="panel">
      <div class="weeks" style="top:150px">
        <section class="week">
          <h3 class="week__title">Week 4</h3>
          <p class="week__text">GP Dr Lena Marsh will share advice about your baby's health in the first 6 months, including:</p>
          <ul class="week__list week__list--cols">
            <li>Skin conditions</li>
            <li>Sleeping</li>
            <li>Crying</li>
            <li>Immunisations</li>
            <li>Fevers and infections</li>
            <li>Colds and coughs</li>
            <li>Teething</li>
            <li>Understanding a baby's signals</li>
          </ul>
        </section>
        <section class="week">
          <h3 class="week__title">Week 5</h3>
          <p class="week__text"><span class="session">Session 1 –</span> Clinical Psychologist Dr Owen Hale will share information about bonding and attachment, your baby's temperament, settling techniques and how to care for yourself.</p>
        </section>
        <section class="week">
          <h3 class="week__title">Week 6</h3>
          <p class="week__text"><span class="session">Session 1 –</span> Dads' Corner – a session for partners about what to expect in the first weeks at home and how to support the new family.</p>
          <p class="week__text"><span class="session">Session 2 –</span> Program review, reflection and evaluation, and how to find local support services once your baby arrives.</p>
        </section>
      </div>
    </article>
  </div>
</section>

</body>
</html>
```